Spa needs a highly desired Membership Card

We need a membership card that captures people's desire to own it(our membership) when flashed by anyone! It should tell the "class" of the card owner!
Comes in Silver & Gold membership. Wants to have same design in different colour/tone to differentiate Gold & Silver.
Most members are woman, but we have few men as well.
Updates
Hi Designers,
Target Market(s)
Woman age 25-55 years old. High spending power in a relatively poor country(Myanmar).
They may be rich businesswomen, wives/daughters of rich man, women who are educated abroad and now return to home country as Myanmar is fast developing.
Requirements
Must have
- Must be in tiff, bmp or jpeg format so that card printer can recognise.
- TEXT
- Velmora Spa (font: Monotype Corsiva)
- No 82, Kintha Street, Mawlin Plaza (Level-5) (7716), Sanchaung Township, Yangon
- 09 47283916
- contactus@tervane-holdco.example
- A space for picture of card owner.
- No magnetic strip/smart chip.
- Name Abcdefghijklmn
- Membership No 12345678
- Expiry MM/YYYY
- For Gold:
- Terms and Conditions
- - Members enjoy 25% off all standard services, excluding promotional offers
- - Members enjoy 5% off for Lumivessa products, excluding promotional items
- - Members enjoy 10% off for all other retail products, excluding promotional items
- - 1 accompanying guest in a day enjoys 20% off standard services, excluding promotional offers
- - Memberships are valid for 2 years from the date of issue and are non-transferable
- - Memberships sold are non-refundable or exchangeable for cash, services or products
- - Privileges are subject to change without prior notice
- For Silver:
- Terms and Conditions
- - Members enjoy 20% off all standard services, excluding promotional offers
- I uploaded 2 of our spa pictures so you can have a feel our of premise. And uploaded our name card, I agree its not stylish as I designed it myself.

```html
<!DOCTYPE html>
<html lang="en">
<head>
<meta charset="UTF-8">
<title>Velmora Spa Membership Cards</title>
<link rel="stylesheet" href="https://fonts.googleapis.com/css2?family=Alegreya+Sans:wght@500;700&family=Dancing+Script:wght@700&family=Marcellus&display=swap">
<style>
  :root {
    --canvas: #ecebe8;
    --card-base: #e9e8e2;
    --quilt-dark: #1f1f21;
    --quilt-mid: #3a3a3d;
    --sky-top: #7fb3c8;
    --navy: #133a63;
    --teal: #2f7c9c;
    --ink: #111111;
    --ink-soft: #2b2b2b;
    --photo-fill: #dcdbd4;
    --gold-1: #f3cf3a;
    --gold-2: #a9561c;
    --gold-3: #fff4a6;
    --gold-solid: #e9b53a;
    --gold-line: #c8922c;
    --silver-1: #d9d9d9;
    --silver-2: #8d8d8d;
    --silver-3: #ffffff;
    --silver-solid: #d6d6d6;
    --silver-line: #9a9a9a;
  }
  * { box-sizing: border-box; margin: 0; padding: 0; }
  html, body { width: 1200px; height: 1000px; overflow: hidden; }
  body { background: var(--canvas); position: relative; }

  .card {
    position: absolute;
    width: 450px;
    height: 256px;
    background: var(--card-base);
    overflow: hidden;
  }
  .card--front-gold   { left: 131px; top: 150px; }
  .card--back-gold    { left: 689px; top: 150px; }
  .card--front-silver { left: 131px; top: 492px; }
  .card--back-silver  { left: 689px; top: 492px; }

  .trim { position: absolute; left: 0; width: 100%; height: 16px; }
  .trim--top { top: 0; }
  .trim--bottom { bottom: 0; }
  .tier-gold .trim {
    background: linear-gradient(90deg, var(--gold-1) 0%, var(--gold-2) 14%, var(--gold-1) 30%, var(--gold-3) 52%, var(--gold-1) 70%, var(--gold-2) 100%);
  }
  .tier-silver .trim {
    background: linear-gradient(90deg, var(--silver-1) 0%, var(--silver-2) 14%, var(--silver-1) 30%, var(--silver-3) 52%, var(--silver-1) 70%, var(--silver-2) 100%);
  }

  /* Front */
  .quilt-band {
    position: absolute; top: 16px; left: 0; width: 100%; height: 65px;
    background: linear-gradient(180deg, var(--quilt-mid), var(--quilt-dark));
  }
  .sky-fade {
    position: absolute; top: 81px; left: 0; width: 100%; height: 46px;
    background: linear-gradient(180deg, var(--sky-top), var(--card-base));
  }
  .brand-name {
    position: absolute; top: 16px; left: 0; width: 100%; height: 65px;
    display: flex; align-items: center; justify-content: center;
    font-family: "Dancing Script", cursive; font-weight: 700; font-size: 46px;
  }
  .tier-gold .brand-name { color: var(--gold-solid); }
  .tier-silver .brand-name { color: var(--silver-solid); }

  .address {
    position: absolute; top: 140px; left: 0; width: 100%;
    text-align: center;
    font-family: "Alegreya Sans", sans-serif; font-weight: 700;
    font-size: 16px; line-height: 21px; color: var(--ink);
  }

  /* Back */
  .ocean-band {
    position: absolute; top: 16px; left: 0; width: 100%; height: 112px;
    background: linear-gradient(180deg, var(--navy) 0%, var(--teal) 45%, var(--card-base) 100%);
  }
  .member-title {
    position: absolute; top: 30px; left: 0; width: 100%;
    text-align: center;
    font-family: "Marcellus", serif; font-size: 60px; letter-spacing: 1px;
    -webkit-background-clip: text; background-clip: text; color: transparent;
  }
  .tier-gold .member-title {
    background-image: linear-gradient(180deg, var(--gold-3) 0%, var(--gold-1) 50%, #d98f1e 100%);
  }
  .tier-silver .member-title {
    background-image: linear-gradient(180deg, var(--silver-3) 0%, var(--silver-1) 50%, var(--silver-2) 100%);
  }

  .owner-photo {
    position: absolute; left: 16px; top: 120px; width: 66px; height: 84px;
    background: var(--photo-fill);
    border: 2px solid var(--gold-line);
  }
  .tier-silver .owner-photo { border-color: var(--silver-line); }

  .member-info {
    position: absolute; left: 94px; right: 14px; top: 119px;
    font-family: "Alegreya Sans", sans-serif; color: var(--ink);
  }
  .member-details {
    list-style: none;
    display: flex; flex-wrap: wrap; column-gap: 14px;
    font-size: 10.5px; line-height: 13px; font-weight: 700;
  }
  .member-details .label { font-weight: 500; color: var(--ink-soft); margin-right: 3px; }
  .terms-title {
    margin-top: 4px;
    font-size: 8.5px; line-height: 10px; font-weight: 700;
  }
  .terms {
    list-style: none;
    font-size: 7.5px; line-height: 9.6px; font-weight: 500; color: var(--ink-soft);
  }
  .terms li::before { content: "– "; }
</style>
</head>
<body>
  <section class="card card--front-gold tier-gold">
    <div class="trim trim--top"></div>
    <div class="quilt-band" role="img" aria-label="Black quilted leather pattern with gold studs"></div>
    <div class="sky-fade"></div>
    <div class="brand-name">Velmora Spa</div>
    <p class="address">No 82, Kintha Street, Mawlin Plaza (Level-5) (7716)<br>Sanchaung Township, Yangon<br>09 47283916<br>contactus@tervane-holdco.example</p>
    <div class="trim trim--bottom"></div>
  </section>

  <section class="card card--back-gold tier-gold">
    <div class="trim trim--top"></div>
    <div class="ocean-band"></div>
    <div class="member-title">MEMBER</div>
    <div class="owner-photo" role="img" aria-label="Space for photo of card owner"></div>
    <div class="member-info">
      <ul class="member-details">
        <li><span class="label">Name</span>Abcdefghijklmn</li>
        <li><span class="label">Membership No</span>12345678</li>
        <li><span class="label">Expiry</span>MM/YYYY</li>
      </ul>
      <p class="terms-title">Terms and Conditions</p>
      <ul class="terms">
        <li>Members enjoy 25% off all standard services, excluding promotional offers</li>
        <li>Members enjoy 5% off for Lumivessa products, excluding promotional items</li>
        <li>Members enjoy 10% off for all other retail products, excluding promotional items</li>
        <li>1 accompanying guest in a day enjoys 20% off standard services, excluding promotional offers</li>
        <li>Memberships are valid for 2 years from the date of issue and are non-transferable</li>
        <li>Memberships sold are non-refundable or exchangeable for cash, services or products</li>
        <li>Privileges are subject to change without prior notice</li>
      </ul>
    </div>
    <div class="trim trim--bottom"></div>
  </section>

  <section class="card card--front-silver tier-silver">
    <div class="trim trim--top"></div>
    <div class="quilt-band" role="img" aria-label="Black quilted leather pattern with silver studs"></div>
    <div class="sky-fade"></div>
    <div class="brand-name">Velmora Spa</div>
    <p class="address">No 82, Kintha Street, Mawlin Plaza (Level-5) (7716)<br>Sanchaung Township, Yangon<br>09 47283916<br>contactus@tervane-holdco.example</p>
    <div class="trim trim--bottom"></div>
  </section>

  <section class="card card--back-silver tier-silver">
    <div class="trim trim--top"></div>
    <div class="ocean-band"></div>
    <div class="member-title">MEMBER</div>
    <div class="owner-photo" role="img" aria-label="Space for photo of card owner"></div>
    <div class="member-info">
      <ul class="member-details">
        <li><span class="label">Name</span>Abcdefghijklmn</li>
        <li><span class="label">Membership No</span>12345678</li>
        <li><span class="label">Expiry</span>MM/YYYY</li>
      </ul>
      <p class="terms-title">Terms and Conditions</p>
      <ul class="terms">
        <li>Members enjoy 20% off all standard services, excluding promotional offers</li>
      </ul>
    </div>
    <div class="trim trim--bottom"></div>
  </section>
</body>
</html>
```